Business card for massage therapy company called Blue Fern Wellness

Need business card for massage therapy company called Blue Fern Wellness. Would like my logo on the front and the back of the card I have 3 options of logos and you can play with what looks better.

Would like this information displayed on the back of the card:

Marcus Ellery
Licensed Massage Therapist
415-903-2264
bluefern-wellness.example
bluefern_wellness_

```html
<!DOCTYPE html>
<html lang="en">
<head>
<meta charset="utf-8">
<title>Blue Fern Wellness – Business Card</title>
<link rel="stylesheet" href="https://fonts.googleapis.com/css2?family=Roboto:wght@400;700&display=swap">
<style>
  :root{
    --page:#2a2a2b;
    --card:#060606;
    --sage:#8b8d7b;
    --copper:#b98a68;
    --ink:#ececec;
  }
  *{box-sizing:border-box;margin:0;padding:0}
  html,body{width:1200px;height:880px;overflow:hidden;background:var(--page)}
  .sheet{position:relative;width:1200px;height:880px}
  .card{
    position:absolute;left:270px;width:660px;height:377px;
    background:var(--card);border-radius:22px;overflow:hidden;
    box-shadow:0 10px 30px rgba(0,0,0,.45);
  }
  .card--front{top:50px}
  .card--back{top:453px}

  .brand{display:flex;align-items:center;gap:18px}
  .brand__mark{width:70px;height:70px;border:2px solid var(--sage);border-radius:50%;flex:none}
  .brand__name{
    font-family:"Roboto",sans-serif;font-weight:400;color:var(--sage);
    font-size:34px;line-height:1.1;white-space:nowrap;
  }

  .card--front .brand{position:absolute;left:50%;top:50%;transform:translate(-50%,-50%)}

  .card--back .brand{position:absolute;left:46px;top:64px}
  .card--back .brand__mark{width:58px;height:58px}
  .card--back .brand__name{font-size:28px}

  .accent-bar{position:absolute;right:0;top:44px;width:14px;height:44px;background:var(--sage)}
  .person{position:absolute;right:60px;top:112px;text-align:right;font-family:"Roboto",sans-serif}
  .person__name{color:var(--sage);font-weight:700;font-size:28px}
  .person__role{color:var(--copper);font-size:18px;margin-top:4px}

  .contacts{position:absolute;left:64px;bottom:46px;list-style:none;font-family:"Roboto",sans-serif;color:var(--ink);font-size:19px}
  .contacts li{display:flex;align-items:center;gap:14px;margin-top:10px}
  .contacts svg{width:20px;height:20px;flex:none}
</style>
</head>
<body>
<main class="sheet">
  <section class="card card--front" aria-label="Card front">
    <div class="brand">
      <div class="brand__mark"></div>
      <p class="brand__name">Blue Fern Wellness</p>
    </div>
  </section>

  <section class="card card--back" aria-label="Card back">
    <div class="accent-bar"></div>

    <div class="brand">
      <div class="brand__mark"></div>
      <p class="brand__name">Blue Fern Wellness</p>
    </div>

    <div class="person">
      <p class="person__name">Marcus Ellery</p>
      <p class="person__role">Licensed Massage Therapist</p>
    </div>

    <ul class="contacts">
      <li>
        <svg viewBox="0 0 24 24" aria-hidden="true"><path fill="#8b8d7b" d="M6.6 10.8a15 15 0 0 0 6.6 6.6l2.2-2.2a1 1 0 0 1 1-.25 11.4 11.4 0 0 0 3.6.57 1 1 0 0 1 1 1V20a1 1 0 0 1-1 1A17 17 0 0 1 3 4a1 1 0 0 1 1-1h3.5a1 1 0 0 1 1 1c0 1.25.2 2.45.57 3.6a1 1 0 0 1-.25 1z"/></svg>
        415-903-2264
      </li>
      <li>
        <svg viewBox="0 0 24 24" aria-hidden="true"><circle cx="12" cy="12" r="9" fill="none" stroke="#8b8d7b" stroke-width="2"/><path d="M3 12h18M12 3c3 3 3 15 0 18M12 3c-3 3-3 15 0 18" fill="none" stroke="#8b8d7b" stroke-width="1.6"/></svg>
        bluefern-wellness.example
      </li>
      <li>
        <svg viewBox="0 0 24 24" aria-hidden="true"><circle cx="12" cy="12" r="9" fill="none" stroke="#8b8d7b" stroke-width="2"/></svg>
        bluefern_wellness_
      </li>
    </ul>
  </section>
</main>
</body>
</html>
```